Aunt's Find Calm - Graphic Pic for Book Cover

I need a BOOK Cover design that has Logo incorporated:
Aunt's Find Calm
Book Size 5x7.

This is a play on the word HIGH - which really is just a feeling people may get when they are out in nature. NOT cartoon looking.

Book Cover Words:
Aunt’s Find Calm: That Edge of the Meadow Glow
PS. No Drugs or Alcohol Needed.

I am writing an inspirational book called Aunt’s Find Calm. It is about hard working, determined mothers with dreams of living the good life while raising successful children along the way. The only problem is that most Mother’s have so many responsibilities that they put upon themselves that sometimes they get stuck in a routine and become fearful of adventure and taking risks. As a result, women lose their sense of freedom and do not take much-needed alone time. Yet, ultimately Mother’s can learn to take a break, which can solve many problems and propel them on to a new trail that may include the high country!
Updates

HI.I am looking forward to your designs!! Added Friday, May 1, 2015

Target Market(s)

Mothers of all ages, from 18 to 80

Logo Text

Aunt's Find Calm

Logo styles of interest
Pictorial/Combination Logo
Colors
f68e4e
f68d4d
faa54b
ffc214
fbed22
f04a50

Requirements
Must have
• Colorful, like sunset colors. Vibrant, Fun...
• Words on it:
• Aunt's Find Calm.
• Edge of the Meadow Glow.
• P.S. No Drugs or Alcohol Needed
Nice to have
• I like the billboard idea with logo in it.
• Road into mountain
• Words on it: Aunt's Find Calm. Edge of the Meadow Glow.
• The book cover, website logo all need to tie together.
Should not have
• Attached are some rough ideas...that I drew up. and a image that might be able to be used.

```html
<!DOCTYPE html>
<html lang="en">
<head>
<meta charset="utf-8">
<title>Aunt's Find Calm — Book Cover</title>
<link rel="stylesheet" href="https://fonts.googleapis.com/css2?family=Pinyon+Script&family=Gentium+Book+Plus&family=Open+Sans:ital,wght@0,700;1,700&display=swap">
<style>
  :root {
    --band: #6b4446;
    --band-text: #eadcd8;
    --paper: #ffffff;
    --title-dark: #2a1214;
    --title-mid: #6e4a4c;
    --accent-orange: #ea5420;
    --brand-brown: #5a3a3c;
    --scene-green: #2fa84f;
    --scene-grey: #6d6a6a;
  }
  * { margin: 0; padding: 0; box-sizing: border-box; }
  html, body { width: 857px; height: 1200px; overflow: hidden; background: var(--paper); }
  .cover { position: relative; width: 857px; height: 1200px; background: var(--paper); }

  .band { position: absolute; left: 0; width: 100%; background: var(--band);
    color: var(--band-text); font-family: "Gentium Book Plus", Georgia, serif;
    display: flex; align-items: center; justify-content: center; letter-spacing: 1px; }
  .band--top { top: 0; height: 128px; font-size: 44px; }
  .band--bottom { bottom: 0; height: 115px; font-size: 46px; }

  .title { font-family: "Pinyon Script", cursive; color: var(--title-dark); position: absolute; line-height: 1; }
  .title__first { left: 20px; top: 150px; font-size: 250px; }
  .title__mid { left: 520px; top: 370px; font-size: 130px; color: var(--title-mid); }
  .title__last { left: 60px; top: 450px; font-size: 300px; }

  .tagline { position: absolute; left: 40px; top: 790px; width: 310px; text-align: center;
    font-family: "Open Sans", Arial, sans-serif; font-style: italic; font-weight: 700;
    font-size: 47px; line-height: 70px; color: var(--accent-orange); }

  .logo-scene { position: absolute; left: 410px; top: 685px; width: 425px; height: 330px;
    border-radius: 8px;
    background: linear-gradient(180deg, var(--scene-green) 0%, #8fcf8f 45%, #c9bfbf 70%, var(--scene-grey) 100%); }
  .brand-name { position: absolute; left: 410px; top: 1020px; width: 425px; text-align: center;
    font-family: "Open Sans", Arial, sans-serif; font-weight: 700; font-size: 34px; color: var(--brand-brown); }
</style>
</head>
<body>
  <main class="cover">
    <header class="band band--top">That Edge of the Meadow Glow</header>

    <h1 class="title-block">
      <span class="title title__first">Aunt’s</span>
      <span class="title title__mid">find</span>
      <span class="title title__last">Calm</span>
    </h1>

    <p class="tagline">No Drugs or Alcohol Needed</p>

    <div class="logo-scene" role="img" aria-label="Mountain and meadow road emblem with the author standing arms outstretched"></div>
    <p class="brand-name">Aunt's Find Calm</p>

    <footer class="band band--bottom">by Carol Wynne</footer>
  </main>
</body>
</html>
```